SEAFOOD PACKAGING (Products for consumer)

We are looking to create packaging for various Tidewell such as octopus and squid. We plan to sell our products in upscale supermarkets.

We are specializing in cut octopus this time.

Please include our company logo. Also, please leave a transparent area so that customers can see the product inside.
Updates

We want to show what is inside, so a picture of the octopus is not required. We need something simple and sophisticated.

Target Market(s)

upscale store in US and ASIA

Industry/Entity Type

Fisheries dealer

Requirements
Must have
• Please include the attached logo,Blue one is preferred.Please leave a transparent part so that the contents of the product can be seen by the consumer.1. product name on packaging →CUT OCTOPUS,TAKO SASHIMI,Highest quality,Top quality etc... 3. What text information should be on the packaging →(It may be edited, but this is the image) The raw materials are caught in a very clean environment and processed in a modern factory with ZEK certification. We are committed to additive-free products. 4. Packing size(cm/inch)→it will be about 19cm*22cm. 5. what kind of packaging do you use →PP or PA 6. dll →ai,jag
Nice to have
• https://quillmora.example/shots/4829174-Velka-Reef We need something simple and sophisticated like this one.
Should not have
• We want to show what is inside, so a picture of the octopus is not required. We need something simple and sophisticated.

```html
<!DOCTYPE html>
<html lang="en">
<head>
<meta charset="utf-8">
<title>Cut Octopus – Tako Sashimi Pack</title>
<link rel="stylesheet" href="https://fonts.googleapis.com/css2?family=Montserrat:ital,wght@0,600;0,700;1,400;1,800&family=Roboto+Condensed:wght@300;400;700&display=swap">
<style>
  :root{
    --navy:#0a1f66;
    --navy-glow:#13339a;
    --ocean:#1a5cff;
    --ocean-soft:#3f7be6;
    --sky:#cdebf3;
    --red:#ff1a10;
    --red-deep:#6d0000;
    --ink-dark:#2a0a0e;
    --white:#ffffff;
  }
  *{box-sizing:border-box;margin:0;padding:0}
  html,body{width:1036px;height:1200px;overflow:hidden;background:var(--white)}
  .pack{position:relative;width:1036px;height:1200px;overflow:hidden;background:var(--white)}
  .pack svg.shapes{position:absolute;inset:0}
  .sea-pattern{position:absolute;left:0;top:790px;width:1036px;height:410px;
    background:linear-gradient(180deg,#e8f1ff 0%,var(--ocean-soft) 55%,#1f5ad8 100%)}
  .maker{position:absolute;left:58px;top:118px;display:flex;align-items:center;gap:10px;
    font-family:"Montserrat",sans-serif;font-weight:700;font-size:34px;color:var(--ocean)}
  .maker .dot{width:22px;height:22px;border-radius:50%;background:var(--ocean)}
  .brand{position:absolute;left:423px;top:48px;width:172px;height:172px;border-radius:50%;
    background:var(--white);display:flex;align-items:center;justify-content:center;gap:8px;
    font-family:"Montserrat",sans-serif;font-weight:700;font-size:32px;color:var(--ocean)}
  .brand .dot{width:14px;height:14px;border-radius:50%;background:var(--ocean)}
  .product-name{position:absolute;left:258px;top:200px;width:503px;height:220px;
    transform:rotate(-9deg);transform-origin:center;font-family:"Montserrat",sans-serif;color:var(--white);text-align:center}
  .product-name .main{display:block;font-weight:800;font-style:italic;font-size:64px;line-height:1;margin-top:56px;letter-spacing:-1px}
  .product-name .sub{display:block;font-weight:400;font-style:italic;font-size:50px;line-height:1;margin-top:4px;padding-left:40px}
  .claim{position:absolute;left:418px;top:464px;width:197px;height:38px;border:1.5px solid var(--white);border-radius:5px;
    font-family:"Roboto Condensed",sans-serif;font-weight:400;font-size:25px;letter-spacing:4px;color:var(--white);
    display:flex;align-items:center;justify-content:center}
  .badge{position:absolute;left:686px;top:748px;width:154px;height:154px;border-radius:50%;background:var(--red);
    border:6px solid var(--ocean);box-shadow:0 0 0 3px var(--white) inset}
  .badge svg{position:absolute;inset:0}
  .story{position:absolute;left:280px;top:937px;width:480px;text-align:center;
    font-family:"Roboto Condensed",sans-serif;font-weight:300;font-size:21px;line-height:29px;color:var(--white)}
  .weight{position:absolute;left:280px;top:1064px;width:480px;text-align:center;
    font-family:"Roboto Condensed",sans-serif;font-weight:700;font-size:30px;color:var(--white);letter-spacing:-0.5px}
  .storage{position:absolute;left:280px;top:1113px;width:480px;text-align:center;
    font-family:"Roboto Condensed",sans-serif;font-weight:400;font-size:22px;color:var(--white)}
</style>
</head>
<body>
<main class="pack">
  <div class="sea-pattern" role="img" aria-label="Blue ocean wave pattern with a line-drawn octopus"></div>

  <svg class="shapes" width="1036" height="1200" viewBox="0 0 1036 1200" aria-hidden="true">
    <defs>
      <linearGradient id="ribbonFill" x1="0" x2="1" y1="0" y2="0">
        <stop offset="0" stop-color="var(--red-deep)"/>
        <stop offset="0.45" stop-color="var(--red)"/>
        <stop offset="1" stop-color="var(--ink-dark)"/>
      </linearGradient>
      <radialGradient id="panelGlow" cx="0.5" cy="0.35" r="0.7">
        <stop offset="0" stop-color="var(--navy-glow)"/>
        <stop offset="1" stop-color="var(--navy)"/>
      </radialGradient>
    </defs>
    <!-- top brand band -->
    <polygon class="brand-band" points="365,0 674,0 674,520 399,613 365,570" fill="var(--navy)"/>
    <line x1="388" y1="0" x2="388" y2="580" stroke="var(--white)" stroke-width="1.2"/>
    <line x1="652" y1="0" x2="652" y2="525" stroke="var(--white)" stroke-width="1.2"/>
    <!-- lower info panel -->
    <polygon class="info-panel" points="261,800 778,800 778,1058 674,1140 674,1200 365,1200 365,1140 261,1058" fill="url(#panelGlow)"/>
    <polyline points="278,820 278,1050 385,1135" fill="none" stroke="var(--ocean)" stroke-width="1.5"/>
    <polyline points="760,820 760,1050 655,1135" fill="none" stroke="var(--ocean)" stroke-width="1.5"/>
    <!-- see-through window -->
    <path class="window" d="M370,653 C480,600 650,520 790,527 C900,532 990,570 1036,600 L1036,905 L840,832 C760,790 700,792 600,805 C480,830 330,850 243,830 C170,800 150,730 153,680 C155,610 220,568 290,570 C350,572 380,610 361,665 Z"
      fill="var(--white)" stroke="var(--ocean)" stroke-width="7" stroke-linejoin="round"/>
    <!-- name ribbon -->
    <path class="ribbon" d="M258,266 C420,250 520,220 600,200 C660,186 720,188 761,194 L761,361 C700,356 640,370 560,392 C450,420 360,430 258,434 Z"
      fill="url(#ribbonFill)" stroke="var(--white)" stroke-width="8" stroke-linejoin="round"/>
  </svg>

  <div class="maker"><span class="dot"></span>Tidewell</div>
  <div class="brand"><span class="dot"></span>Marlo</div>

  <h1 class="product-name"><span class="main">CUT OCTOPUS</span><span class="sub">TAKO SASHIMI</span></h1>

  <div class="claim">ALL NATURAL</div>

  <div class="badge">
    <svg width="142" height="142" viewBox="0 0 142 142">
      <defs>
        <path id="badgeRing" d="M71,71 m-50,0 a50,50 0 1,1 100,0 a50,50 0 1,1 -100,0"/>
      </defs>
      <circle cx="71" cy="71" r="36" fill="none" stroke="var(--white)" stroke-width="1.5"/>
      <text font-family="Montserrat, sans-serif" font-weight="600" font-size="17" fill="var(--white)" letter-spacing="1.5">
        <textPath href="#badgeRing" startOffset="0">NO ADDITIVES • NO ADDITIVES •</textPath>
      </text>
      <path d="M71,48 C79,60 86,68 86,78 A15,15 0 0 1 56,78 C56,68 63,60 71,48 Z" fill="var(--white)"/>
    </svg>
  </div>

  <p class="story">The raw materials are caught in a very clean environment processed in a modern factory with ZEK certification</p>
  <p class="weight">NET WT. 32 OZ (2.0 LB) 907g</p>
  <p class="storage">KEEP FROZEN</p>
</main>
</body>
</html>
```